Meridian Vault Data Systems Needs a Website Desing

We need a website design for a new company based in Kuwait called Meridian Vault Data Systems (MVDS). We provide Software as a Service (SaaS) solutions for small and medium business companies. We will develop the required E-systems like HR,Payroll,Accounting Systems for those customers who wants to focus on their business instead of wasting time to automate it. MVDS need a web site that represent this activity and showing our cloud products and allow out customers to easily identify their needs. as a normal web site basic things need to be included like :
about MVDS
Solutions
PressRoom
Contact us
please i need something similar to qorlix.com or tuv.com or www.hxp7zul.com with blue and black theme .. please check the Company's logo
hi all ,,,
the project is only design without any codes
Reason: The project is focus on design only ,, i will be really appreciated to have more designs

```html
<!DOCTYPE html>
<html lang="en">
<head>
<meta charset="utf-8">
<title>Meridian Vault Data Systems</title>
<link rel="stylesheet" href="https://fonts.googleapis.com/css2?family=Open+Sans:wght@400;600;800&family=Cinzel:wght@400;600&family=Audiowide&family=Noto+Serif:wght@400;700&display=swap">
<style>
  :root {
    --page-dark: #0c0e11;
    --page-mid: #1a1d22;
    --header-white: #ffffff;
    --ink: #1b1b1b;
    --cyan-pale: #dafcfd;
    --cyan-soft: #a8eaf1;
    --cyan-line: #4fe3f2;
    --cyan-text: #3ad3e6;
    --cloud-top: #d8f6fd;
    --cloud-bottom: #5fc3ee;
    --button-ink: #0a3552;
    --banner-deep: #020a2a;
    --banner-blue: #0a3fa8;
    --banner-glow: #3b8cf0;
    --banner-text: #a9f2fb;
    --social-slot: #2f6fb5;
  }
  * { box-sizing: border-box; margin: 0; padding: 0; }
  html, body { width: 1200px; height: 1000px; overflow: hidden; }
  body {
    position: relative;
    background: radial-gradient(ellipse at 50% 70%, var(--page-mid), var(--page-dark) 75%);
    font-family: "Open Sans", sans-serif;
  }

  /* header */
  .site-header { position: absolute; left: 0; top: 25px; width: 1200px; height: 153px; background: var(--header-white); }
  .brand { position: absolute; left: 35px; top: 42px; display: flex; align-items: center; gap: 12px; color: var(--ink); }
  .brand-mark { width: 92px; height: 92px; border-radius: 50%; background: var(--cloud-bottom); flex: none; }
  .brand-name { font-family: "Open Sans", sans-serif; font-weight: 800; line-height: 1; }
  .brand-name .short { display: block; font-size: 80px; letter-spacing: 6px; }
  .brand-name .long { display: block; font-size: 14.5px; margin-top: 2px; }
  .header-art { position: absolute; left: 695px; top: 5px; width: 312px; height: 120px; border-radius: 120px 120px 0 0;
    background: linear-gradient(var(--cloud-top), var(--cloud-bottom)); }
  .social-slot { position: absolute; top: 70px; width: 42px; height: 42px; border-radius: 6px; background: var(--social-slot); }
  .account-links { position: absolute; left: 1040px; top: 33px; font-family: "Cinzel", serif; font-weight: 600; font-size: 26px; color: #333; line-height: 36px; text-align: center; width: 140px; }
  .search-field { position: absolute; left: 686px; top: 148px; width: 345px; height: 36px; border: 3px solid #111; border-radius: 8px; background: #fff; }
  .search-button { position: absolute; left: 1037px; top: 148px; width: 154px; height: 36px; border: 3px solid #111; border-radius: 8px; background: var(--cyan-pale);
    font-family: "Cinzel", serif; font-size: 22px; color: #222; display: flex; align-items: center; justify-content: center; gap: 6px; }

  /* navigation */
  .main-nav { position: absolute; left: 3px; top: 195px; width: 1194px; height: 55px; border-radius: 6px;
    background: linear-gradient(var(--cyan-pale), var(--cyan-soft)); display: flex; align-items: center; justify-content: space-between; padding: 0 42px 0 45px;
    font-size: 29px; color: #111; box-shadow: 0 3px 6px rgba(0,0,0,.5); }
  .main-nav .dot { font-size: 22px; }

  /* hero banner */
  .hero { position: absolute; left: 12px; top: 252px; width: 1178px; height: 340px;
    background: radial-gradient(ellipse at 70% 40%, var(--banner-glow) 0%, var(--banner-blue) 30%, var(--banner-deep) 80%); }
  .hero-title { position: absolute; left: 66px; top: 32px; font-family: "Audiowide", sans-serif; font-size: 46px; letter-spacing: 4px; color: var(--banner-text); transform: skewX(-12deg); text-shadow: 2px 3px 4px rgba(0,0,0,.6); }
  .hero-sub { position: absolute; left: 148px; top: 106px; font-family: "Audiowide", sans-serif; font-size: 29px; letter-spacing: 5px; color: var(--banner-text); transform: skewX(-12deg); text-shadow: 2px 3px 4px rgba(0,0,0,.6); }

  /* content */
  .presenter-photo { position: absolute; left: 10px; top: 620px; width: 205px; height: 330px; border-radius: 90px 90px 10px 10px; background: linear-gradient(#3a2a22, #1d1f24); }
  .content-frame { position: absolute; left: 228px; top: 610px; width: 964px; height: 348px; border: 2px solid var(--cyan-line); border-radius: 10px; box-shadow: 0 0 8px var(--cyan-line); }
  .intro-box { position: absolute; left: 248px; top: 763px; width: 922px; height: 177px; border: 2px solid var(--cyan-line); box-shadow: 0 0 6px var(--cyan-line); }
  .service-button { position: absolute; top: 640px; width: 168px; height: 80px; border-radius: 24px;
    background: linear-gradient(var(--cloud-top), var(--cloud-bottom));
    display: flex; align-items: center; justify-content: center; text-align: center;
    font-family: "Noto Serif", serif; font-weight: 700; font-size: 12px; color: var(--button-ink); }
  .service-button::after { content: ""; position: absolute; left: 26px; top: 103px; width: 110px; height: 5px; border-radius: 50%; background: #ddd; }
  .cloud-art { position: absolute; left: 275px; top: 780px; width: 190px; height: 140px; border-radius: 60px; background: radial-gradient(circle, #bff0fb, #3c8fc7 70%, transparent 72%); }
  .intro-text { position: absolute; left: 478px; top: 794px; width: 690px; font-family: "Noto Serif", serif; font-size: 20.5px; line-height: 30px; color: var(--cyan-text); }

  /* footer */
  .site-footer { position: absolute; left: 28px; top: 966px; width: 1130px; display: flex; justify-content: space-between; font-family: "Cinzel", serif; font-weight: 600; font-size: 18px; color: var(--cyan-text); text-transform: uppercase; }
  .site-footer .legal { letter-spacing: .3px; }
</style>
</head>
<body>
  <header class="site-header">
    <div class="brand">
      <span class="brand-mark"></span>
      <span class="brand-name"><span class="short">MVDS</span><span class="long">Meridian Vault Data Systems</span></span>
    </div>
    <div class="header-art" role="img" aria-label="Light blue cloud illustration holding the social links"></div>
    <span class="social-slot" style="left:780px"></span>
    <span class="social-slot" style="left:836px"></span>
    <span class="social-slot" style="left:892px"></span>
    <div class="account-links"><div>Login</div><div>Register</div></div>
  </header>
  <div class="search-field"></div>
  <div class="search-button">Search
    <svg width="20" height="20" viewBox="0 0 20 20" aria-hidden="true"><circle cx="8" cy="8" r="6" fill="none" stroke="#222" stroke-width="2.5"/><line x1="12.5" y1="12.5" x2="18" y2="18" stroke="#222" stroke-width="3"/></svg>
  </div>

  <nav class="main-nav">
    <span>HOME</span><span class="dot">•</span><span>ABOUT US</span><span class="dot">•</span><span>SOLUTIONS</span><span class="dot">•</span><span>PRODUCTS</span><span class="dot">•</span><span>PRESS ROOM</span><span class="dot">•</span><span>CAREERS</span>
  </nav>

  <section class="hero" role="img" aria-label="Abstract glowing blue waves with light particles">
    <div class="hero-title">BEST SOLUTIONS</div>
    <div class="hero-sub">for small and medium business companies</div>
  </section>

  <div class="presenter-photo" role="img" aria-label="Photo of a smiling businesswoman with arms crossed"></div>
  <div class="content-frame"></div>

  <a class="service-button" style="left:292px">CLOUD SERVICES</a>
  <a class="service-button" style="left:512px">VIRTUALISATION</a>
  <a class="service-button" style="left:732px">COMPANY</a>
  <a class="service-button" style="left:952px">SUPPORT &amp; DOWNLOADS</a>

  <div class="intro-box"></div>
  <div class="cloud-art" role="img" aria-label="Cloud computing illustration with connected devices"></div>
  <p class="intro-text">We provide Software as a Service (SaaS) solutions for small and medium business companies. We will develop the required E-systems like HR,Payroll,Accounting Systems for those customers who wants to focus on their business instead of wasting time to automate it.</p>

  <footer class="site-footer">
    <span>© Copyright 2013,MVDS,Inc. All Rights Reserved</span>
    <span class="legal">Contact Us•Terms of Use•Privacy•Help•Feedback</span>
  </footer>
</body>
</html>
```